Brackenford Fluidworks needs a website describing the repair business we are in.

Brackenford Fluidworks is a full hydraulic repair facility. We have 2 shops. We repair and service all hydraulic cylinders, pneumatic cylinders, hydraulic pumps, motors, valves and gearboxes. Our services range from large industrial plants to the individual that owns one piece of equipment. We also offer removal and install of cylinders. Along with free pick up and delivery, within a certain distance which is usually 100 miles from one of our shops.

With over 30 years experience in the hydraulic business, we can repair or replace any job. There is not a job too big or too small, we service them all.

We have customers that send whole pieces of equipment to us to do complete overhauls on all the hydraulics. Ranging from a country club green roller to a 10 ton boom truck.

Target Market(s)

Industrial plants, road builders, dirt work companies, general contractors, owners of industrial equipment (bulldozers, excavators, loaders, scrapers, motor graders, etc.

Industry/Entity Type

Hydraulic

Number of Pages Required

5+ page

Font styles to use
Sans Serif

Colors
ec1f27
ffffff
aaaaaa

Requirements
Must have
• Information about what we offer and pictures of jobs completed.
Nice to have
• Nice stock photos of jobsites and industrial plants.
Should not have
• Any sort of comical characters.

```html
<!DOCTYPE html>
<html lang="en">
<head>
<meta charset="utf-8">
<title>Brackenford Fluidworks</title>
<link href="https://fonts.googleapis.com/css2?family=Roboto:wght@400;500;700;900&family=Open+Sans:wght@400;600;700&display=swap" rel="stylesheet">
<style>
:root{
  --red:#ec1f27;
  --red-soft:#e9555b;
  --white:#ffffff;
  --grey:#aaaaaa;
  --ink:#222222;
  --text:#555555;
  --black:#0b0b0b;
  --panel:#efefef;
}
*{box-sizing:border-box;margin:0;padding:0}
html,body{width:1200px;height:3186px;overflow:hidden}
body{position:relative;background:var(--white);font-family:"Open Sans",Arial,sans-serif;color:var(--text)}
.abs{position:absolute}
.head{font-family:"Roboto",Arial,sans-serif}

/* header */
.site-header{position:absolute;left:0;top:0;width:1200px;height:148px;background:var(--white)}
.brand{position:absolute;left:98px;top:24px;width:140px;text-align:center}
.brand-dot{width:62px;height:62px;border-radius:50%;background:var(--red);margin:0 auto 8px}
.brand-name{font-family:"Roboto",Arial,sans-serif;font-weight:700;font-size:17px;line-height:19px;color:var(--red);text-transform:uppercase}
.contact-strip{position:absolute;top:32px;right:99px;display:flex;align-items:center;gap:10px;font-size:15px;color:var(--ink)}
.contact-strip .ico{width:32px;height:32px;border-radius:50%;display:flex;align-items:center;justify-content:center}
.contact-strip .ico.dark{background:#444}
.contact-strip .ico.red{background:var(--red)}
.contact-strip .gap{width:16px}
.contact-strip .phone{color:var(--red)}
.socials{display:flex;gap:5px;margin-left:12px}
.socials span{width:22px;height:22px;background:var(--grey)}
.socials span:nth-child(odd){background:#8a8a8a}
.main-nav{position:absolute;top:102px;right:98px;display:flex;gap:35px;font-family:"Roboto",Arial,sans-serif;font-size:16px;font-weight:500;color:var(--ink);text-transform:uppercase}
.main-nav .active{color:var(--red)}

/* hero */
.hero{position:absolute;left:0;top:148px;width:1200px;height:552px;background:linear-gradient(180deg,#4b4640 0%,#5a544c 45%,#3f3a34 100%);overflow:hidden}
.hero-title{position:absolute;top:76px;width:100%;text-align:center;color:var(--white);font-family:"Roboto",Arial,sans-serif;font-weight:700;font-size:48px}
.hero-text{position:absolute;top:162px;left:270px;width:660px;text-align:center;color:var(--white);font-size:15px;font-weight:600;line-height:28px}
.hero-btn{position:absolute;left:537px;top:260px;width:126px;height:48px;border:2px solid var(--white);border-radius:3px;color:var(--white);font-family:"Roboto",Arial,sans-serif;font-weight:500;font-size:15px;display:flex;align-items:center;justify-content:center}
.hero-arrow{position:absolute;top:222px}
.hero-curve{position:absolute;left:0;bottom:0}

/* services */
.service{position:absolute;top:567px;width:300px;text-align:center}
.service-ring{width:246px;height:246px;border-radius:50%;border:12px solid var(--red-soft);margin:0 auto;overflow:hidden;position:relative}
.service-ring .photo{position:absolute;inset:0}
.service-ring.hover .photo{background:var(--red)!important}
.service h3{font-family:"Roboto",Arial,sans-serif;font-weight:500;font-size:19px;color:var(--ink);margin-top:32px;text-transform:uppercase}
.service p{font-size:13px;line-height:21px;margin:16px auto 0;width:280px}
.service .more{margin-top:20px;font-family:"Roboto",Arial,sans-serif;font-size:14px;font-weight:700;color:var(--ink);display:flex;justify-content:center;align-items:center;gap:8px}
.service .more.on{color:var(--red)}

/* features */
.features{position:absolute;left:0;top:1056px;width:1200px;height:562px;background:linear-gradient(180deg,#121212,#050505 60%,#151515)}
.section-title{position:absolute;width:100%;text-align:center;font-family:"Roboto",Arial,sans-serif;font-weight:700;font-size:31px;text-transform:uppercase}
.title-rule{position:absolute;left:560px;width:80px;height:2px}
.feature{position:absolute;top:190px;width:240px;text-align:center;color:var(--white)}
.feature svg{display:block;margin:0 auto}
.feature h4{font-family:"Roboto",Arial,sans-serif;font-weight:500;font-size:20px;margin-top:20px;text-transform:uppercase}
.feature p{font-size:12.5px;font-weight:600;line-height:21px;margin-top:12px}

/* projects */
.projects-intro{position:absolute;top:1744px;left:160px;width:880px;text-align:center;font-size:13px;line-height:23px}
.project{position:absolute;top:1833px;width:289px;height:223px}
.project::after{content:"";position:absolute;inset:10px 10px;border:2px solid rgba(255,255,255,.8)}
.btn{position:absolute;top:2109px;height:43px;display:flex;align-items:center;justify-content:center;color:var(--white);font-family:"Roboto",Arial,sans-serif;font-weight:500;font-size:14px;border-radius:2px}

/* testimonials */
.testimonials{position:absolute;left:0;top:2222px;width:1200px;height:499px;background:var(--panel)}
.review{position:absolute;top:207px;width:470px}
.avatar{position:absolute;left:0;top:0;width:116px;height:116px;border-radius:50%;border:5px solid #d9d9d9;background:linear-gradient(160deg,#c9b9a6,#8f7f70)}
.quote{position:absolute;left:90px;top:-10px;color:var(--red);font-family:"Roboto",Arial,sans-serif;font-weight:900;font-size:48px;line-height:48px}
.review h5{position:absolute;left:125px;top:20px;font-family:"Roboto",Arial,sans-serif;font-weight:500;font-size:22px;color:#444;white-space:nowrap}
.review .who{position:absolute;left:125px;top:54px;font-size:14px;color:#777}
.review .stars{position:absolute;left:125px;top:82px}
.review p{position:absolute;left:0;top:177px;width:470px;font-size:13px;line-height:23px;color:#666}

/* footer */
.site-footer{position:absolute;left:0;top:2721px;width:1200px;height:465px;background:var(--black);color:var(--white)}
.foot-brand{position:absolute;left:98px;top:120px;width:175px;text-align:center}
.foot-brand .brand-dot{background:var(--white);width:84px;height:84px;margin-bottom:12px}
.foot-brand .brand-name{color:var(--white);font-size:21px;line-height:24px}
.foot-col h6{font-family:"Roboto",Arial,sans-serif;font-weight:500;font-size:16px;text-transform:uppercase}
.foot-col h6::after{content:"";display:block;width:100px;height:2px;background:var(--white);margin-top:10px}
.foot-col{position:absolute;top:76px}
.quick li{list-style:none;font-size:14px;margin-top:14px}
.quick li:first-child{margin-top:24px}
.info{display:flex;gap:14px;margin-top:24px}
.info .ring{width:40px;height:40px;border-radius:50%;border:2px solid var(--white);flex:none;display:flex;align-items:center;justify-content:center}
.info b{font-family:"Roboto",Arial,sans-serif;font-size:14px;text-transform:uppercase}
.info div{font-size:13px;line-height:20px}
.field{position:absolute;border:1px solid #ccc;border-radius:3px;font-size:11px;color:#ddd;padding:8px 10px}
.send{position:absolute;background:var(--red);font-size:11px;font-weight:600;display:flex;align-items:center;justify-content:center;text-transform:uppercase}
.foot-rule{position:absolute;left:98px;top:380px;width:1004px;height:1px;background:#bbb}
.copyright{position:absolute;left:98px;top:417px;font-size:13px;font-weight:600}
.foot-social{position:absolute;left:948px;top:408px;display:flex;gap:9px}
.foot-social span{width:34px;height:34px;border-radius:50%;border:2px solid var(--white)}
</style>
</head>
<body>

<header class="site-header">
  <div class="brand"><div class="brand-dot"></div><div class="brand-name">Brackenford Fluidworks</div></div>
  <div class="contact-strip">
    <span class="ico dark"><svg width="16" height="12" viewBox="0 0 16 12"><rect x="0.5" y="0.5" width="15" height="11" fill="none" stroke="#fff"/><path d="M1 1l7 6 7-6" fill="none" stroke="#fff"/></svg></span>
    <span>info@brackenfordfluidworks.com</span>
    <span class="gap"></span>
    <span class="ico red"><svg width="16" height="16" viewBox="0 0 24 24"><path fill="#fff" d="M6.6 10.8a15 15 0 006.6 6.6l2.2-2.2c.3-.3.7-.4 1-.2 1.1.4 2.3.6 3.6.6.6 0 1 .4 1 1V20c0 .6-.4 1-1 1A17 17 0 013 4c0-.6.4-1 1-1h3.5c.6 0 1 .4 1 1 0 1.3.2 2.5.6 3.6.1.3 0 .7-.2 1z"/></svg></span>
    <span class="phone">+180 555 0147</span>
    <div class="socials"><span></span><span></span><span></span><span></span><span></span></div>
  </div>
  <nav class="main-nav"><span class="active">Home</span><span>About Us</span><span>Blog</span><span>Commercial</span><span>Industrial</span><span>Contact Us</span></nav>
</header>

<section class="hero" role="img" aria-label="Workshop photo of hydraulic cylinders laid on timber pallets">
  <h1 class="hero-title">BRACKENFORD FLUIDWORKS</h1>
  <p class="hero-text">Brackenford Fluidworks is a full hydraulic repair facility. We have 2 shops. We repair and service all hydraulic cylinders, pneumatic cylinders.</p>
  <div class="hero-btn">Read More</div>
  <svg class="hero-arrow" style="left:34px" width="28" height="52" viewBox="0 0 28 52"><path d="M26 2L2 26l24 24" fill="none" stroke="#fff" stroke-width="2"/></svg>
  <svg class="hero-arrow" style="right:34px" width="28" height="52" viewBox="0 0 28 52"><path d="M2 2l24 24L2 50" fill="none" stroke="#fff" stroke-width="2"/></svg>
  <svg class="hero-curve" width="1200" height="552" viewBox="0 0 1200 552"><path d="M0 457Q600 647 1200 457V552H0Z" fill="#fff"/></svg>
</section>

<article class="service" style="left:96px">
  <div class="service-ring"><div class="photo" role="img" aria-label="Red hydraulic cylinder on workbench" style="background:linear-gradient(160deg,#6b5c54,#a1483c 55%,#4d4540)"></div></div>
  <h3>Hydraulic Cylinders</h3>
  <p>Duis aute irure dolor in reprehenderit in vo luptate velit esse cillum dolore eu fugiat nulla pariatur. Excepteur sint occaecat.</p>
  <div class="more">READ MORE <svg width="14" height="14" viewBox="0 0 14 14"><circle cx="7" cy="7" r="7" fill="#222"/><path d="M5.5 4l3 3-3 3" fill="none" stroke="#fff" stroke-width="1.6"/></svg></div>
</article>
<article class="service" style="left:455px">
  <div class="service-ring hover"><div class="photo" role="img" aria-label="Pneumatic cylinder photo under red overlay"></div>
    <svg style="position:absolute;left:89px;top:96px" width="44" height="30" viewBox="0 0 44 30"><path d="M2 15C9 4 35 4 42 15 35 26 9 26 2 15Z" fill="none" stroke="#fff" stroke-width="3"/><circle cx="22" cy="15" r="6" fill="#fff"/></svg></div>
  <h3>Pneumatic Cylinders</h3>
  <p>Duis aute irure dolor in reprehenderit in vo luptate velit esse cillum dolore eu fugiat nulla pariatur. Excepteur sint occaecat.</p>
  <div class="more on">READ MORE <svg width="14" height="14" viewBox="0 0 14 14"><circle cx="7" cy="7" r="7" fill="#ec1f27"/><path d="M5.5 4l3 3-3 3" fill="none" stroke="#fff" stroke-width="1.6"/></svg></div>
</article>
<article class="service" style="left:804px">
  <div class="service-ring"><div class="photo" role="img" aria-label="Yellow hydraulic pump with hoses" style="background:linear-gradient(150deg,#3b3a36,#c9a82a 50%,#5a564e)"></div></div>
  <h3>Hydraulic Pumps</h3>
  <p>Duis aute irure dolor in reprehenderit in vo luptate velit esse cillum dolore eu fugiat nulla pariatur. Excepteur sint occaecat.</p>
  <div class="more">READ MORE <svg width="14" height="14" viewBox="0 0 14 14"><circle cx="7" cy="7" r="7" fill="#222"/><path d="M5.5 4l3 3-3 3" fill="none" stroke="#fff" stroke-width="1.6"/></svg></div>
</article>

<section class="features" role="img" aria-label="Dark photo of a trailer carrying hydraulic cylinders">
  <h2 class="section-title" style="top:70px;color:#fff">Our Features</h2>
  <div class="title-rule" style="top:130px;background:#fff"></div>

  <div class="feature" style="left:75px">
    <svg width="212" height="212" viewBox="0 0 212 212"><circle cx="106" cy="106" r="100" fill="none" stroke="#bbb" stroke-width="10"/><path d="M16 62A100 100 0 01150 16" fill="none" stroke="#ec1f27" stroke-width="10"/><circle cx="106" cy="106" r="90" fill="#fff"/>
      <g fill="#ec1f27"><rect x="100" y="82" width="40" height="9" rx="4"/><rect x="100" y="95" width="40" height="9" rx="4"/><rect x="100" y="108" width="40" height="9" rx="4"/><rect x="100" y="121" width="40" height="9" rx="4"/><circle cx="90" cy="112" r="20"/></g>
      <text x="90" y="120" text-anchor="middle" fill="#fff" font-family="Roboto,Arial,sans-serif" font-weight="700" font-size="22">$</text></svg>
    <h4>Our Values</h4><p>Nemo enim ipsam voluptatem quia voluptas sit aspernatur aut odit aut fugit.</p>
  </div>
  <div class="feature" style="left:345px">
    <svg width="212" height="212" viewBox="0 0 212 212"><circle cx="106" cy="106" r="100" fill="none" stroke="#bbb" stroke-width="10"/><path d="M16 62A100 100 0 01150 16" fill="none" stroke="#ec1f27" stroke-width="10"/><circle cx="106" cy="106" r="90" fill="#fff"/>
      <g fill="none" stroke="#ec1f27" stroke-width="4"><circle cx="98" cy="90" r="14"/><path d="M72 134c0-18 12-26 26-26 6 0 11 1 15 4"/><path d="M118 110l14 5v10c0 8-6 13-14 16-8-3-14-8-14-16v-10z"/></g></svg>
    <h4>Safety</h4><p>Nemo enim ipsam voluptatem quia voluptas sit aspernatur aut odit aut fugit.</p>
  </div>
  <div class="feature" style="left:611px">
    <svg width="212" height="212" viewBox="0 0 212 212"><circle cx="106" cy="106" r="100" fill="none" stroke="#bbb" stroke-width="10"/><path d="M16 62A100 100 0 01150 16" fill="none" stroke="#ec1f27" stroke-width="10"/><circle cx="106" cy="106" r="90" fill="#fff"/>
      <g fill="none" stroke="#ec1f27" stroke-width="4"><rect x="80" y="102" width="12" height="34"/><path d="M92 104l12-18c4-5 10-2 9 4l-3 12h18c5 0 7 4 6 8l-5 20c-1 4-4 6-8 6H92"/><path d="M106 70v-12M90 74l-6-8M122 74l6-8"/></g></svg>
    <h4>Quality</h4><p>Nemo enim ipsam voluptatem quia voluptas sit aspernatur aut odit aut fugit.</p>
  </div>
  <div class="feature" style="left:876px">
    <svg width="212" height="212" viewBox="0 0 212 212"><circle cx="106" cy="106" r="100" fill="none" stroke="#bbb" stroke-width="10"/><path d="M16 62A100 100 0 01150 16" fill="none" stroke="#ec1f27" stroke-width="10"/><circle cx="106" cy="106" r="90" fill="#fff"/>
      <g fill="#ec1f27"><rect x="74" y="98" width="12" height="30"/><path d="M88 100l12-18c4-5 10-2 9 4l-3 12h14v30H88z"/></g>
      <path d="M110 118l10 10 20-26" fill="none" stroke="#ec1f27" stroke-width="5"/></svg>
    <h4>Reliability</h4><p>Nemo enim ipsam voluptatem quia voluptas sit aspernatur aut odit aut fugit.</p>
  </div>
</section>

<h2 class="section-title" style="top:1686px;color:var(--red)">Recent Projects</h2>
<p class="projects-intro">Nemo enim ipsam voluptatem quia voluptas sit aspernatur aut odit aut fugit, sed quia consequuntur magni dolores eos qui ratione voluptatem sequi nesciunt. Neque porro quisquam est, qui dolorem ipsum quia dolor sit amet.</p>
<div class="project" style="left:8px;background:linear-gradient(160deg,#8b8d8f,#3a3236 55%,#6e6f70)" role="img" aria-label="Black cylinders lying on shop floor"></div>
<div class="project" style="left:308px;background:linear-gradient(160deg,#4d4a47,#c0a170 40%,#d86a22 75%,#5b5650)" role="img" aria-label="Orange cylinder on timber pallet"></div>
<div class="project" style="left:605px;background:linear-gradient(160deg,#6f6a63,#8e3f34 55%,#b9a27c)" role="img" aria-label="Red cylinder resting on pallets in workshop"></div>
<div class="project" style="left:905px;background:linear-gradient(160deg,#8a8278,#a74737 50%,#c3ae88)" role="img" aria-label="Repaired red cylinders on pallet"></div>
<div class="btn" style="left:459px;width:138px;background:var(--red)">More Projects</div>
<div class="btn" style="left:605px;width:134px;background:#444">Our Services</div>

<section class="testimonials">
  <h2 class="section-title" style="top:68px;color:var(--red)">Our Testimonials</h2>
  <div class="title-rule" style="left:553px;width:94px;top:128px;background:var(--red)"></div>

  <div class="review" style="left:102px">
    <div class="avatar" style="left:24px" role="img" aria-label="Customer portrait"></div>
    <div class="quote" style="left:170px">"</div>
    <h5 style="left:205px">Good Service</h5><div class="who" style="left:205px">Marla Quinn</div>
    <svg class="stars" style="left:205px" width="92" height="16" viewBox="0 0 92 16"><g fill="#ec1f27"><path id="s" d="M8 0l2.4 5 5.6.8-4 3.9 1 5.5L8 12.6 3 15.2l1-5.5-4-3.9 5.6-.8z"/><use href="#s" x="19"/><use href="#s" x="38"/><use href="#s" x="57"/></g><path transform="translate(76 0)" d="M8 0l2.4 5 5.6.8-4 3.9 1 5.5L8 12.6 3 15.2l1-5.5-4-3.9 5.6-.8z" fill="none" stroke="#ec1f27"/></svg>
    <p>Neque porro quisquam est, qui dolorem ipsum quia dolor sit amet, consecte tur, adipisci velit, sed quia non numquam eius modi tempora.</p>
  </div>
  <div class="review" style="left:639px">
    <div class="avatar" style="left:24px" role="img" aria-label="Customer portrait"></div>
    <div class="quote" style="left:170px">"</div>
    <h5 style="left:205px">Great Response</h5><div class="who" style="left:205px">Tom Reddick</div>
    <svg class="stars" style="left:205px" width="92" height="16" viewBox="0 0 92 16"><g fill="#ec1f27"><use href="#s"/><use href="#s" x="19"/><use href="#s" x="38"/><use href="#s" x="57"/></g><path transform="translate(76 0)" d="M8 0l2.4 5 5.6.8-4 3.9 1 5.5L8 12.6 3 15.2l1-5.5-4-3.9 5.6-.8z" fill="none" stroke="#ec1f27"/></svg>
    <p>Neque porro quisquam est, qui dolorem ipsum quia dolor sit amet, consecte tur, adipisci velit, sed quia non numquam.</p>
  </div>
</section>

<footer class="site-footer">
  <div class="foot-brand"><div class="brand-dot"></div><div class="brand-name">Brackenford Fluidworks</div></div>

  <div class="foot-col" style="left:350px">
    <h6>Quick Links</h6>
    <ul class="quick"><li>› Home</li><li>› About Us</li><li>› Blog</li><li>› Commercial</li><li>› Industrial</li><li>› Contact Us</li></ul>
  </div>

  <div class="foot-col" style="left:518px;width:260px">
    <h6>Contact Us</h6>
    <div class="info"><span class="ring"><svg width="14" height="18" viewBox="0 0 14 18"><path d="M7 0a7 7 0 017 7c0 5-7 11-7 11S0 12 0 7a7 7 0 017-7z" fill="#fff"/><circle cx="7" cy="7" r="2.5" fill="#0b0b0b"/></svg></span><div><b>Address,</b><br>Lower Ashcombe, Western<br>Australia, 6190.</div></div>
    <div class="info"><span class="ring"><svg width="12" height="18" viewBox="0 0 12 18"><rect x="1" y="1" width="10" height="16" rx="2" fill="none" stroke="#fff" stroke-width="2"/></svg></span><div><b>Phone:</b><br>+180 555 0147</div></div>
    <div class="info"><span class="ring"><svg width="16" height="12" viewBox="0 0 16 12"><rect width="16" height="12" fill="#fff"/><path d="M0 0l8 7 8-7" fill="none" stroke="#0b0b0b" stroke-width="1.5"/></svg></span><div><b>Mail:</b><br>info@brackenfordfluidworks.com</div></div>
  </div>

  <div class="foot-col" style="left:813px;width:287px">
    <h6>Contact Form</h6>
  </div>
  <div class="field" style="left:813px;top:127px;width:139px;height:36px">Name</div>
  <div class="field" style="left:961px;top:127px;width:139px;height:36px">Phone</div>
  <div class="field" style="left:813px;top:172px;width:287px;height:66px">Message</div>
  <div class="send" style="left:813px;top:254px;width:119px;height:38px">Send Message</div>

  <div class="foot-rule"></div>
  <div class="copyright">Copyrights © 2018 Brackenford Fluidworks. All Rights Reserved.</div>
  <div class="foot-social"><span></span><span></span><span></span><span></span></div>
</footer>

</body>
</html>
```